8x8 Social Media Ad - Summit Harbor Expo

Attention Real Estate Agents
Please join us for our
Quarterly Real Estate Training Expo
The 2nd Saturday of February, May, August and November
Our Next Training Expo is _________________________________
From 9 am to 1 pm
at
Marlowe Suites Fernfield Oak Ridge
4187 Copper Meadow Lane, Fernfield, MD 20994
Scheduled Speakers
9:00 am - Malcolm Prewitt - Orientation
9:30 am - Darnell Ockley - Multiple Income Streams / Pivot Program
10:00 am - Keira Lindqvist - Marketing though Social Media
10:45 am - Owen Trask - Generating Business through Lumo-Net
11:30 am - Ada Nwachime - Real Estate Investing
12:15 pm - Gregory Tamsin - (Main Speaker) Training Topic TBA
For more information call Malcolm Prewitt at (240) 555-0182 or email mprewitt@summitharborhomes.example

```html
<!DOCTYPE html>
<html lang="en">
<head>
<meta charset="utf-8">
<title>Summit Harbor Expo – Quarterly Real Estate Training Expo</title>
<link rel="stylesheet" href="https://fonts.googleapis.com/css2?family=Anton&family=Oswald:wght@400;500&display=swap">
<style>
  :root {
    --backdrop: #8a8a8a;
    --teal: #0a8f98;
    --teal-deep: #067580;
    --teal-bright: #18d3df;
    --cyan-text: #1fd0dc;
    --black: #050505;
    --white: #ffffff;
    --silver-light: #f4f4f4;
    --silver-mid: #c9c9c9;
    --silver-dark: #9a9a9a;
    --placeholder-face: #b9b4b0;
  }
  * { box-sizing: border-box; margin: 0; padding: 0; }
  html, body { width: 1200px; height: 1117px; overflow: hidden; }
  body { background: var(--backdrop); position: relative; font-family: "Anton", sans-serif; color: var(--white); }

  .ad { position: absolute; left: 133px; top: 104px; width: 933px; height: 933px; overflow: hidden; background: var(--teal); }

  .silver-top { position: absolute; left: 0; top: 0; width: 933px; height: 19px;
    background: linear-gradient(90deg, var(--silver-dark), var(--silver-light) 30%, var(--silver-mid) 60%, var(--silver-light) 85%, var(--silver-dark)); }

  .hero-photo { position: absolute; left: 0; top: 19px; width: 933px; height: 528px;
    background:
      linear-gradient(90deg, rgba(0,0,0,1) 0%, rgba(0,0,0,.92) 28%, rgba(0,0,0,.2) 55%, rgba(0,0,0,0) 70%),
      radial-gradient(ellipse at 78% 70%, #c8743a 0%, #7a4a2e 30%, #2c3f5c 60%, #1d4f86 100%); }

  .shapes { position: absolute; left: 0; top: 0; width: 933px; height: 933px; }

  .brand { position: absolute; left: 690px; top: 42px; width: 220px; text-align: center; color: var(--teal-deep); line-height: 1; }
  .brand-name { font-size: 42px; letter-spacing: 1px; }
  .brand-sub { font-size: 15px; letter-spacing: 1px; margin-top: 8px; }

  .headline-lead { position: absolute; left: 50px; top: 46px; font-size: 44px; line-height: 1; text-shadow: 3px 3px 0 var(--black); letter-spacing: -.5px; white-space: nowrap; }
  .headline-main { position: absolute; left: 50px; top: 112px; font-size: 54px; line-height: 1; letter-spacing: -.5px; white-space: nowrap; }
  .headline-big { position: absolute; left: 49px; top: 172px; font-size: 93px; line-height: 1; letter-spacing: -1px; white-space: nowrap;
    background: linear-gradient(180deg, #ffffff 0%, #e6e6e6 40%, #9e9e9e 70%, #e8e8e8 100%);
    -webkit-background-clip: text; background-clip: text; color: transparent;
    filter: drop-shadow(4px 4px 0 var(--black)); }

  .schedule-day { position: absolute; left: 50px; top: 293px; line-height: 1; }
  .schedule-day .ordinal { font-size: 52px; letter-spacing: -1px; }
  .schedule-day .ordinal small { font-size: 21px; vertical-align: 20px; margin-right: 4px; }
  .schedule-day .weekday { font-size: 53px; letter-spacing: -1px; margin-top: 1px; }
  .schedule-day .hours { font-size: 31px; margin-top: 3px; letter-spacing: -.5px; }

  .months { position: absolute; left: 262px; top: 298px; list-style: none; }
  .months li { display: flex; align-items: center; height: 34.5px; font-family: "Oswald", sans-serif; font-weight: 500; font-size: 35px; line-height: 1; letter-spacing: -1px; transform: scaleX(.92); transform-origin: left; }
  .months svg { width: 24px; height: 24px; margin-right: 15px; flex: none; }

  .venue { position: absolute; left: 51px; top: 451px; color: var(--cyan-text); font-size: 24px; line-height: 26px; letter-spacing: -.3px; white-space: nowrap; }

  .speakers-title { position: absolute; left: 0; top: 547px; width: 933px; text-align: center; font-family: "Oswald", sans-serif; font-weight: 500; font-size: 27px; letter-spacing: 14px; line-height: 1; margin-top: -2px; padding-left: 14px; }

  .speakers { position: absolute; left: 0; top: 590px; width: 933px; height: 240px; }
  .speaker { position: absolute; top: 0; width: 140px; margin-left: -70px; text-align: center; }
  .speaker-photo { width: 120px; height: 120px; margin: 0 auto; border-radius: 50%; background: var(--white); padding: 7px; box-shadow: 0 8px 12px rgba(0,0,0,.3); }
  .speaker-photo span { display: block; width: 100%; height: 100%; border-radius: 50%; background: radial-gradient(circle at 50% 40%, var(--placeholder-face), #6d6a68); }
  .speaker-time { margin-top: 11px; font-size: 18px; line-height: 20px; }
  .speaker-name { font-size: 18px; line-height: 21px; letter-spacing: -.4px; white-space: nowrap; }
  .speaker-topic { font-family: "Oswald", sans-serif; font-weight: 400; font-size: 14px; line-height: 15.5px; text-transform: uppercase; letter-spacing: -.3px; }

  .contact { position: absolute; left: 0; top: 826px; width: 933px; text-align: center; line-height: 1; letter-spacing: -.5px; white-space: nowrap; }
  .contact-line { display: block; font-size: 40px; height: 42px; }
  .contact-line.email-line { font-size: 33px; height: 40px; padding-top: 4px; }
</style>
</head>
<body>
  <main class="ad">
    <div class="silver-top"></div>
    <div class="hero-photo" role="img" aria-label="Photo of a modern two-storey house with warm lit wood siding at dusk"></div>

    <svg class="shapes" viewBox="0 0 933 933" aria-hidden="true">
      <defs>
        <linearGradient id="silver" x1="0" y1="0" x2="1" y2="0">
          <stop offset="0" stop-color="#b5b5b5"/>
          <stop offset=".35" stop-color="#f6f6f6"/>
          <stop offset=".7" stop-color="#c4c4c4"/>
          <stop offset="1" stop-color="#efefef"/>
        </linearGradient>
        <linearGradient id="tealBand" x1="0" y1="0" x2="1" y2="0">
          <stop offset="0" stop-color="#0a8f98"/>
          <stop offset=".5" stop-color="#15c3ce"/>
          <stop offset="1" stop-color="#0a8f98"/>
        </linearGradient>
        <radialGradient id="tealPanel" cx=".5" cy="0" r=".8">
          <stop offset="0" stop-color="#0fb2bd"/>
          <stop offset="1" stop-color="#0a8f98"/>
        </radialGradient>
      </defs>
      <polygon points="618,19 933,19 933,157 676,157" fill="url(#silver)"/>
      <polygon points="0,95 476,95 579,273 0,273" fill="#050505"/>
      <polygon points="0,40 446,40 464,95 0,95" fill="url(#tealBand)"/>
      <polyline points="470,60 506,60 597,273 0,273" fill="none" stroke="#18d3df" stroke-width="2"/>
      <rect x="0" y="547" width="933" height="24" fill="url(#silver)"/>
      <rect x="0" y="571" width="933" height="362" fill="url(#tealPanel)"/>
      <polygon points="217,530 718,530 727,571 208,571" fill="#0a8f98"/>
      <polyline points="0,573 208,573 217,530 718,530 727,573 933,573" fill="none" stroke="#18d3df" stroke-width="2"/>
    </svg>

    <div class="brand">
      <div class="brand-name">SUMMIT HARBOR</div>
      <div class="brand-sub">REALTY GROUP</div>
    </div>

    <h1>
      <span class="headline-lead">PLEASE JOIN US FOR OUR</span>
      <span class="headline-main">QUARTERLY REAL ESTATE</span>
      <span class="headline-big">TRAINING EXPO</span>
    </h1>

    <div class="schedule-day">
      <div class="ordinal"><small>THE</small>2ND</div>
      <div class="weekday">SATURDAY</div>
      <div class="hours">9 AM TO 1 PM</div>
    </div>

    <ul class="months">
      <li><svg viewBox="0 0 24 24"><circle cx="12" cy="12" r="12" fill="#18d3df"/><path d="M6.5 12.5l3.5 3.5 7-7" fill="none" stroke="#050505" stroke-width="3"/></svg>FEBRUARY</li>
      <li><svg viewBox="0 0 24 24"><circle cx="12" cy="12" r="12" fill="#18d3df"/><path d="M6.5 12.5l3.5 3.5 7-7" fill="none" stroke="#050505" stroke-width="3"/></svg>MAY</li>
      <li><svg viewBox="0 0 24 24"><circle cx="12" cy="12" r="12" fill="#18d3df"/><path d="M6.5 12.5l3.5 3.5 7-7" fill="none" stroke="#050505" stroke-width="3"/></svg>AUGUST</li>
      <li><svg viewBox="0 0 24 24"><circle cx="12" cy="12" r="12" fill="#18d3df"/><path d="M6.5 12.5l3.5 3.5 7-7" fill="none" stroke="#050505" stroke-width="3"/></svg>NOVEMBER</li>
    </ul>

    <p class="venue">AT MARLOWE SUITES FERNFIELD OAK RIDGE 4187<br>COPPER MEADOW LANE, FERNFIELD, MD 20994</p>

    <h2 class="speakers-title">SCHEDULED SPEAKERS</h2>

    <section class="speakers">
      <div class="speaker" style="left:113px">
        <div class="speaker-photo"><span role="img" aria-label="Portrait of Malcolm Prewitt"></span></div>
        <div class="speaker-time">9:00 AM</div>
        <div class="speaker-name">MALCOLM PREWITT</div>
        <div class="speaker-topic">Orientation</div>
      </div>
      <div class="speaker" style="left:251px">
        <div class="speaker-photo"><span role="img" aria-label="Portrait of Darnell Ockley"></span></div>
        <div class="speaker-time">9:30 AM</div>
        <div class="speaker-name">DARNELL OCKLEY</div>
        <div class="speaker-topic">Multiple Income<br>Streams /<br>Pivot Program</div>
      </div>
      <div class="speaker" style="left:399px">
        <div class="speaker-photo"><span role="img" aria-label="Portrait of Keira Lindqvist"></span></div>
        <div class="speaker-time">10:00 AM</div>
        <div class="speaker-name">KEIRA LINDQVIST</div>
        <div class="speaker-topic">Marketing though<br>Social Media</div>
      </div>
      <div class="speaker" style="left:549px">
        <div class="speaker-photo"><span role="img" aria-label="Portrait of Owen Trask"></span></div>
        <div class="speaker-time">10:45 AM</div>
        <div class="speaker-name">OWEN TRASK</div>
        <div class="speaker-topic">Generating<br>Business through<br>Lumo-Net</div>
      </div>
      <div class="speaker" style="left:690px">
        <div class="speaker-photo"><span role="img" aria-label="Portrait of Ada Nwachime"></span></div>
        <div class="speaker-time">11:30 AM</div>
        <div class="speaker-name">ADA NWACHIME</div>
        <div class="speaker-topic">Real Estate<br>Investing</div>
      </div>
      <div class="speaker" style="left:822px">
        <div class="speaker-photo"><span role="img" aria-label="Portrait of Gregory Tamsin"></span></div>
        <div class="speaker-time">12:15 PM</div>
        <div class="speaker-name">GREGORY TAMSIN</div>
        <div class="speaker-topic">(Main Speaker)<br>Training Topic TBA</div>
      </div>
    </section>

    <p class="contact">
      <span class="contact-line">FOR MORE INFORMATION CALL MALCOLM PREWITT</span>
      <span class="contact-line email-line">AT (240) 555-0182 OR EMAIL MPREWITT@SUMMITHARBORHOMES.EXAMPLE</span>
    </p>
  </main>
</body>
</html>
```